Label for a new chocolate snack

Hello. We are Meadow Treat House. We are a new company making healthy chocolate snacks. We need Labels for our first product: Rosie's Chocolate Dates,

We have two varieties:

1) dark chocolate

2) milk chocolate

The labels are 4 inches wide by 6 inches height. They are being printed on white glossy paper. They will be going on Kraft bags.

Here is the info we need on the labels:

Rosie's
Chocolate Dates
Peanut Butter Center
Milk Chocolate
8g of Protein
Great Source of Energy
175g.

Rosies Chocolate Dates are targeted towards women who are 20-45 years of age.
Our goal is to create products that are healthy and taste good at the same time.

Finally, we will be adding more variations in the future, such as almond butter center, so being able to change the theme of the label to match the center filling would be good.

Thank you to everyone who will be submitting a design and good luck.

Target Market(s)

Woman, 20-40 years old, shop at gourmet grocery stores and health food stores

Industry/Entity Type

It Company

Colors

Designer to choose colors to be used in the design.

Requirements
Must have
• Rosie's
• Chocolate Dates
• Peanut Butter Centre
• Milk Chocolate / Dark Chocolate
• 8g of Protein
• Great Source of Energy
• 175g.
• Back side of label must have everything contained in the pdfs i have attached.
• We are looking for a upscale chocolate look. That will still stand out on the shelf.
Should not have
• Main colors should not be brown, or black.

```html
<!DOCTYPE html>
<html lang="en">
<head>
<meta charset="UTF-8">
<title>Rosie's Chocolate Dates – Milk Chocolate Label</title>
<link href="https://fonts.googleapis.com/css2?family=Oswald:wght@300;400;500&display=swap" rel="stylesheet">
<style>
  :root {
    --cream: #f8efcb;
    --red: #c8202f;
    --red-dark: #9e1522;
    --cocoa: #5a3a1e;
    --ink: #3a2a1e;
    --white: #ffffff;
    --photo-light: #e9d8b4;
    --photo-mid: #8a5a36;
    --photo-dark: #4a2c18;
  }
  * { margin: 0; padding: 0; box-sizing: border-box; }
  html, body { width: 800px; height: 1200px; overflow: hidden; background: var(--cream); }
  .label {
    position: relative;
    width: 800px;
    height: 1200px;
    background: var(--cream);
    overflow: hidden;
    font-family: "Oswald", "Arial Narrow", sans-serif;
  }
  .corner-flag {
    position: absolute;
    top: 0; left: 0;
    width: 300px; height: 300px;
  }
  .brand-name {
    position: absolute;
    top: 78px; left: 0; width: 100%;
    text-align: center;
    font-family: "Oswald", "Arial Narrow", sans-serif;
    font-weight: 300;
    font-size: 62px;
    letter-spacing: 10px;
    text-transform: uppercase;
    color: var(--cocoa);
    line-height: 1;
  }
  .product-title {
    position: absolute;
    top: 240px; left: 0; width: 100%;
    text-align: center;
    color: var(--red);
    font-weight: 400;
    line-height: 1;
    text-transform: uppercase;
  }
  .product-title .line-one { display: block; font-size: 108px; letter-spacing: 1px; }
  .product-title .line-two { display: block; font-size: 184px; letter-spacing: 4px; margin-top: -4px; }
  .variety-ribbon {
    position: absolute;
    top: 508px; left: 190px;
    width: 420px; height: 58px;
  }
  .variety-ribbon span {
    position: absolute; inset: 0;
    display: flex; align-items: center; justify-content: center;
    color: var(--white);
    font-size: 36px;
    letter-spacing: 1px;
    text-transform: uppercase;
  }
  .product-photo {
    position: absolute;
    top: 645px; left: 245px;
    width: 555px; height: 455px;
    border-radius: 40% 0 0 30% / 45% 0 0 25%;
    background: radial-gradient(ellipse at 60% 40%, var(--photo-mid) 0%, var(--photo-dark) 45%, var(--photo-light) 78%, var(--cream) 100%);
  }
  .badge { position: absolute; }
  .badge-energy { top: 718px; left: 47px; width: 140px; height: 140px; }
  .badge-protein { top: 918px; left: 50px; width: 134px; height: 134px; }
  .net-weight {
    position: absolute;
    top: 1130px; left: 0; width: 100%;
    text-align: center;
    font-weight: 300;
    font-size: 32px;
    line-height: 1;
    color: var(--ink);
  }
</style>
</head>
<body>
<div class="label">
  <svg class="corner-flag" viewBox="0 0 300 300">
    <polygon points="0,0 300,0 0,300" fill="var(--red)"/>
    <g transform="translate(95,95) rotate(-45)" fill="var(--white)" font-family="Oswald, sans-serif" font-size="30" text-anchor="middle">
      <text x="0" y="-8">PEANUT</text>
      <text x="0" y="28">BUTTER CENTER</text>
    </g>
  </svg>

  <div class="brand-name">Rosie's</div>

  <h1 class="product-title">
    <span class="line-one">Chocolate</span>
    <span class="line-two">Dates</span>
  </h1>

  <div class="variety-ribbon">
    <svg width="420" height="58" viewBox="0 0 420 58">
      <polygon points="0,6 22,29 0,52 30,52 30,6" fill="var(--red-dark)"/>
      <polygon points="420,6 398,29 420,52 390,52 390,6" fill="var(--red-dark)"/>
      <rect x="18" y="0" width="384" height="58" fill="var(--red)"/>
    </svg>
    <span>Milk Chocolate</span>
  </div>

  <div class="product-photo" role="img" aria-label="Chocolate-coated dates with mint leaves, stacked milk chocolate pieces and a spoon of peanut butter"></div>

  <svg class="badge badge-energy" viewBox="0 0 132 132" role="img" aria-label="Great source of energy">
    <defs>
      <path id="energy-arc" d="M 18 66 A 48 48 0 0 1 114 66"/>
    </defs>
    <circle cx="66" cy="66" r="60" fill="none" stroke="var(--cocoa)" stroke-width="2"/>
    <text font-family="Oswald, sans-serif" font-size="12" fill="var(--cocoa)" letter-spacing="0.5">
      <textPath href="#energy-arc" startOffset="50%" text-anchor="middle">GREAT SOURCE OF ENERGY</textPath>
    </text>
    <circle cx="66" cy="76" r="22" fill="none" stroke="var(--red)" stroke-width="4"/>
    <path d="M 56 76 L 64 84 L 78 68" fill="none" stroke="var(--red)" stroke-width="4" stroke-linecap="round"/>
  </svg>

  <svg class="badge badge-protein" viewBox="0 0 132 132" role="img" aria-label="8g of protein">
    <defs>
      <path id="protein-arc" d="M 14 70 A 52 52 0 0 0 118 70"/>
    </defs>
    <circle cx="66" cy="60" r="46" fill="none" stroke="var(--cocoa)" stroke-width="4"/>
    <text x="66" y="78" text-anchor="middle" font-family="Oswald, sans-serif" font-size="48" fill="var(--cocoa)">8g</text>
    <text font-family="Oswald, sans-serif" font-size="13" fill="var(--cocoa)">
      <textPath href="#protein-arc" startOffset="50%" text-anchor="middle">OF PROTEIN</textPath>
    </text>
  </svg>

  <div class="net-weight">Net Wt.175g</div>
</div>
</body>
</html>
```